Paws About Town Helpers

Design a flyer (A5 - I think!) with bright colours to promote an in home Dog Service.
Include an animated picture of a dog (being walked/playing/jumping etc)
Bold Heading, list of services with animated pictures, contact details

Industry/Entity Type

It Service

Requirements
Must have
• Add price list to back of A5 Flyer with same colours and design as front page of flyer - See Attached.

```html
<!DOCTYPE html>
<html lang="en">
<head>
<meta charset="utf-8">
<title>Paws About Town Helpers – Dog Services Flyer</title>
<link href="https://fonts.googleapis.com/css2?family=Jost:wght@400;600;700;800&display=swap" rel="stylesheet">
<style>
  :root {
    --backdrop: #6e6e6e;
    --cream: #fbf1c4;
    --stripe: #f6e08f;
    --teal: #3aa89a;
    --teal-dark: #2a7f74;
    --panel-brown: #6b3418;
    --panel-brown-light: #8a4a22;
    --card-orange: #d9742c;
    --card-yellow: #f4cd6e;
    --text-brown: #4e230c;
    --white: #ffffff;
    --ink: #161616;
    --dog-orange: #d97a34;
    --dog-orange-dark: #c4662a;
  }
  * { box-sizing: border-box; margin: 0; padding: 0; }
  html, body {
    width: 1200px; height: 1000px; overflow: hidden;
    background: var(--backdrop);
    font-family: "Jost", "Century Gothic", sans-serif;
  }
  .flyer {
    position: absolute; left: 280px; top: 40px;
    width: 640px; height: 920px; overflow: hidden;
    background: repeating-linear-gradient(90deg, var(--cream) 0 22px, var(--stripe) 22px 44px);
  }
  .title-ribbon {
    position: absolute; left: 40px; top: 28px; width: 560px; height: 56px;
    background: var(--teal); border-radius: 6px;
    display: flex; align-items: center; justify-content: center;
    color: var(--white); font-weight: 700; font-size: 31px; letter-spacing: 1px;
    text-transform: uppercase; z-index: 3;
    box-shadow: 0 3px 0 var(--teal-dark);
  }
  .services-panel {
    position: absolute; left: 36px; top: 60px; width: 568px; height: 640px;
    background: linear-gradient(180deg, var(--panel-brown-light), var(--panel-brown));
    border-radius: 22px; border: 6px solid var(--cream);
  }
  .service-card {
    position: absolute; width: 250px;
    background: var(--card-orange); border-radius: 14px;
    overflow: hidden; text-align: center; text-transform: uppercase;
    box-shadow: 0 0 0 3px var(--card-orange), inset 0 0 0 2px rgba(255,255,255,.45);
  }
  .service-card .tag {
    position: absolute; top: 8px; left: 50%; width: 64px; height: 16px;
    margin-left: -32px; background: var(--white); border-radius: 8px;
  }
  .service-card h2 {
    color: var(--white); font-weight: 800; font-size: 19px; line-height: 1.05;
    padding: 34px 16px 12px;
  }
  .service-card p {
    background: var(--card-yellow); color: var(--text-brown);
    font-weight: 700; font-size: 14px; line-height: 1.15;
    padding: 12px 18px 14px;
  }
  .card-poop { left: 36px; top: 50px; }
  .card-feed { left: 36px; top: 225px; }
  .card-bath { left: 36px; top: 420px; }
  .card-walk { left: 300px; top: 100px; }
  .card-play { left: 300px; top: 285px; }
  .dog-illustration {
    position: absolute; left: 355px; top: 555px; width: 265px; height: 150px; z-index: 4;
    background: linear-gradient(160deg, var(--dog-orange), var(--dog-orange-dark));
    border-radius: 80px 80px 30px 30px;
  }
  .footer {
    position: absolute; left: 0; top: 640px; width: 640px; height: 280px; z-index: 5;
  }
  .footer svg { position: absolute; inset: 0; }
  .footer-text {
    position: absolute; left: 0; right: 0; top: 90px; text-align: center; color: var(--ink);
  }
  .footer-call { font-weight: 800; font-size: 20px; text-transform: uppercase; letter-spacing: .5px; }
  .footer-name { font-weight: 600; font-size: 38px; margin: 10px 0 12px; }
  .footer-contact { font-weight: 400; font-size: 22px; letter-spacing: .5px; }
</style>
</head>
<body>
  <div class="flyer">
    <div class="title-ribbon">Paws About Town Helpers</div>

    <div class="services-panel">
      <div class="service-card card-poop"><span class="tag"></span>
        <h2>Tired of picking up dog poop?</h2><p>Arrange for us to do it for you!</p></div>
      <div class="service-card card-feed"><span class="tag"></span>
        <h2>Can't get home in time to feed our dog?</h2><p>Use our dog feeding service!</p></div>
      <div class="service-card card-bath"><span class="tag"></span>
        <h2>Dog needs a bath?</h2><p>We'll arrange for a professional to keep it clean!</p></div>
      <div class="service-card card-walk"><span class="tag"></span>
        <h2>Need a break from walking the dog?</h2><p>We will come and collect your dog and take it for a walk!</p></div>
      <div class="service-card card-play"><span class="tag"></span>
        <h2>Want someone to play with your dog while you're at work?</h2><p>We will be your dog's best buddy!</p></div>
    </div>

    <div class="dog-illustration" role="img" aria-label="Cartoon of a happy orange dachshund trotting along with its tongue out and a teal collar"></div>

    <div class="footer">
      <svg viewBox="0 0 640 280" preserveAspectRatio="none" aria-hidden="true">
        <defs>
          <linearGradient id="footerFill" x1="0" y1="0" x2="1" y2="1">
            <stop offset="0" stop-color="#d8edf6"/>
            <stop offset="1" stop-color="#a9d2e6"/>
          </linearGradient>
        </defs>
        <path d="M0 60 Q320 0 640 60 L640 280 L0 280 Z" fill="url(#footerFill)"/>
        <path d="M0 60 Q320 0 640 60" fill="none" stroke="#3aa89a" stroke-width="8"/>
        <path d="M20 82 Q320 28 620 82" fill="none" stroke="#8cc3d8" stroke-width="2" stroke-dasharray="2 6"/>
      </svg>
      <div class="footer-text">
        <div class="footer-call">For all services related to your dog – call PATH</div>
        <div class="footer-name">“Paws About Town Helpers”</div>
        <div class="footer-contact">0400 123 456 | www.pawsabouttownhelpers.com.au</div>
      </div>
    </div>
  </div>
</body>
</html>
```